Health & Fitness Author & Public Speaker Needs Visually Stunning Web Redesign!

It's time for a redesign of the home page for Beatrix Holloway's "Bright Fork Kitchen" website (www.brightforkkitchen.example). We have a VERY clear idea of what we want, so it really won't take a talented designer long to bring it to life.
The website itself is used to promote & sell her range of health & nutrition programs to a female audience, primarily aged 24 - 35 working in professional or semi professional occupations.
For a VERY comprehensive outline of exactly what we are after, please see the following attached files:
(1) 'Website - WireFrame' (layout, content/copy, visual design style we want along with the desired color scheme)
(2) 'Website - Style Guide' (these are the colours, and overall feel we want)
PLEASE REVIEW THIS IN FULL - THEY WILL GIVE YOU A VERY CLEAR IDEA OF WHAT WE WANT.
Most of the files you need are attached, but for more photos that you can use (of Beatrix, her programs, and food/meals) can be found at these URL's:
BEATRIX (profile photos):
https://www.filevault.example/s/k3m9p2x7q1/AbCdEf1234
ECOVERS
- Bright Fork Kitchen Guide (ebook): https://www.filevault.example/s/r8t4w6y2n5/GhIjKl5678
- 6 Week Total Momentum Course (ecourse): https://www.filevault.example/s/u1v5z9c3b7/MnOpQr9012
- E-Magazine Issues:
https://www.filevault.example/s/d2f6h8j4l0/StUvWx3456
STOCK IMAGES:
https://www.filevault.example/s/g7k1m5n9p3/YzAbCd7890
As we will need to revamp our existing Facebook page & other printed material, there may be the potential for further work for the successful designer in the future.
Thanks & Good Luck!
Desmond Farrow
Marketing & Business Development Manager
Bright Fork Kitchen

```html
<!DOCTYPE html>
<html lang="en">
<head>
<meta charset="utf-8">
<title>Bright Fork Kitchen – Home</title>
<link href="https://fonts.googleapis.com/css2?family=Ubuntu:wght@400;500;700&family=Open+Sans:wght@400;600;700&display=swap" rel="stylesheet">
<style>
:root{
  --pink:#e0166e;
  --teal:#2fb0b2;
  --teal-dark:#2c8f9c;
  --ink:#3d3d3d;
  --body:#555;
  --muted:#8a8a8a;
  --band:#ededed;
  --line:#cfcfcf;
  --white:#fff;
  --orange:#f39a1e;
}
*{box-sizing:border-box;margin:0;padding:0}
html,body{width:1200px;height:2516px;overflow:hidden;background:var(--white)}
body{position:relative;font-family:"Open Sans",Arial,sans-serif;color:var(--body)}
.abs{position:absolute}

/* hero */
.hero{left:0;top:0;width:1200px;height:448px;background:linear-gradient(100deg,#f1e3cf 0%,#e9c89a 35%,#d9b07c 60%,#a99174 100%)}
.hero-figure{right:70px;top:40px;width:340px;height:408px;background:linear-gradient(180deg,#c98f6a,#7d5a48 55%,#3d7fb8 80%,#2f6da6);border-radius:160px 160px 0 0;opacity:.9}
.brand{left:26px;top:40px;font-family:"Ubuntu",sans-serif;font-weight:700;font-size:38px;color:var(--ink);display:flex;align-items:center;gap:12px}
.brand-dot{width:34px;height:34px;border-radius:50%;background:var(--pink)}
.nav{right:24px;top:42px;font-family:"Ubuntu",sans-serif;font-weight:700;font-size:16px;color:#666;letter-spacing:.3px}
.nav span{margin:0 8px;color:#999}
.hero-title{left:38px;top:226px;width:632px;padding:6px 14px;background:rgba(60,60,60,.72);font-family:"Ubuntu",sans-serif;font-weight:500;font-size:39px;line-height:44px;color:var(--white);text-transform:uppercase}

/* top sign-up band */
.optin{left:0;top:448px;width:1200px;height:96px;background:var(--pink);color:var(--white)}
.optin h2{position:absolute;left:42px;top:14px;font-family:"Ubuntu",sans-serif;font-weight:500;font-size:26px}
.optin p{position:absolute;left:42px;top:52px;width:480px;font-size:13px;line-height:16px;font-weight:600}
.envelope{position:absolute;left:530px;top:16px;width:62px;height:62px;border-radius:50%;background:var(--orange);border:4px solid #fbd08a}
.field{position:absolute;height:29px;background:var(--white);border:1px solid #ddd;font-size:12px;color:#888;padding:6px 8px}
.btn{position:absolute;background:var(--teal-dark);color:var(--white);font-family:"Ubuntu",sans-serif;font-weight:700;text-align:center}

/* main column */
.main{left:62px;top:568px;width:806px}
.main h1{font-family:"Ubuntu",sans-serif;font-weight:500;font-size:35px;line-height:42px;color:var(--teal)}
.main p{font-size:13px;line-height:20px;color:var(--body);margin-top:10px}
.main h3{font-family:"Ubuntu",sans-serif;font-weight:700;font-size:21px;color:var(--ink)}
.ticks{list-style:none}
.ticks li{position:relative;padding-left:34px;font-size:13px;line-height:20px;min-height:29px;padding-top:4px}
.ticks li::before{content:"";position:absolute;left:0;top:4px;width:18px;height:18px;border:2px solid #666;border-radius:3px}
.ticks li::after{content:"";position:absolute;left:6px;top:2px;width:7px;height:14px;border:solid #333;border-width:0 3px 3px 0;transform:rotate(40deg)}
.video{position:relative;margin:30px 0 0 112px;width:472px;height:296px;border:1px solid var(--line);background:#fafafa;box-shadow:0 8px 10px -6px rgba(0,0,0,.3);padding:10px}
.video-still{width:100%;height:100%;background:linear-gradient(180deg,#a8c7e6 0%,#cfd9e0 45%,#8a7a60 70%,#6e6650 100%)}
.play{position:absolute;left:218px;top:125px;width:38px;height:28px;background:#c4131a;border-radius:6px}
.play::after{content:"";position:absolute;left:14px;top:7px;border-left:12px solid #fff;border-top:7px solid transparent;border-bottom:7px solid transparent}
.video-bar{position:absolute;left:10px;right:10px;bottom:10px;height:24px;background:#f4f4f4;border-top:3px solid #ccc}
.video-bar::before{content:"";position:absolute;left:0;top:-3px;width:90px;height:3px;background:#d11}

/* sidebar */
.side{left:906px;width:238px;border:1px solid var(--line)}
.found{top:568px;height:191px;padding:10px 12px}
.found h4{font-family:"Ubuntu",sans-serif;font-size:12px;font-weight:700;color:var(--ink)}
.badge{position:absolute;height:22px;background:#d7d7d7;border-radius:2px}
.kick{top:776px;height:236px;background:linear-gradient(180deg,#e3e3e3,#b9b9b9)}
.kick-band{position:absolute;left:0;right:0;bottom:0;height:70px;background:var(--pink);color:#fff;text-align:center;padding-top:8px}
.kick-band b{display:block;font-family:"Ubuntu",sans-serif;font-size:14px}
.kick-band span{font-size:10px;line-height:12px;display:block;padding:0 8px}
.order{top:1030px;height:325px;background:#fff}
.ribbon{position:absolute;left:10px;right:10px;top:6px;height:34px;background:var(--pink);color:#fff;font-family:"Ubuntu",sans-serif;font-weight:700;font-size:17px;text-align:center;line-height:34px}
.order-art{position:absolute;left:20px;top:56px;width:196px;height:150px;background:linear-gradient(135deg,#f2f2f2,#d9c6cf 50%,#cf7ea0)}
.order p{position:absolute;left:14px;right:14px;top:214px;font-size:11px;line-height:14px;color:#777;text-align:center}
.buy{position:absolute;left:0;right:0;bottom:0;height:62px;background:#dcdcdc;font-family:"Ubuntu",sans-serif;font-weight:700;font-size:22px;color:#333;padding:16px 0 0 80px}
.buy-bag{position:absolute;left:16px;top:10px;width:42px;height:42px;background:#8dbf3c;border-radius:4px}
.buy-arrow{position:absolute;right:18px;top:24px;border-left:16px solid var(--pink);border-top:8px solid transparent;border-bottom:8px solid transparent}
.emag{top:1372px;height:264px;background:#fff;overflow:hidden}
.emag-art{position:absolute;left:14px;top:12px;width:208px;height:178px;background:linear-gradient(135deg,#f6e3ec,#c7d9e3 50%,#e7b7c9)}
.emag b{position:absolute;left:14px;top:200px;font-family:"Ubuntu",sans-serif;font-size:14px;color:var(--ink)}
.emag span{position:absolute;left:14px;top:220px;font-size:11px;color:var(--pink)}
.corner{position:absolute;right:-32px;bottom:8px;width:110px;height:24px;background:var(--pink);transform:rotate(-45deg);color:#fff;font-weight:700;font-size:12px;text-align:center;line-height:24px}
.social-like{left:906px;top:1653px;width:238px;font-size:9px;color:#666;display:flex;gap:6px;align-items:flex-start}
.social-like i{font-style:normal;background:#5b74a8;color:#fff;padding:2px 4px;font-weight:700}

/* bottom band */
.lower-band{left:0;top:2180px;width:1200px;height:278px;background:var(--band)}
.portrait{left:104px;top:2185px;width:148px;height:273px;background:linear-gradient(180deg,#6b4a3c 0%,#c79a86 35%,#8a4c9e 65%,#5b3b72 100%);border-radius:70px 70px 0 0}
.mail-icon{left:273px;top:2209px;width:64px;height:48px;border:3px solid #b5b5b5;background:#fff;overflow:hidden}
.mail-icon::after{content:"";position:absolute;left:9px;top:-24px;width:40px;height:40px;border:solid #b5b5b5;border-width:0 3px 3px 0;transform:rotate(45deg)}
.lower-title{left:352px;top:2206px;width:370px;font-family:"Ubuntu",sans-serif;font-weight:400;font-size:23px;line-height:28px;color:#555}
.lower-copy{left:273px;top:2284px;width:390px;font-size:13px;line-height:18px;color:#666}
.cta-title{left:752px;top:2206px;font-family:"Ubuntu",sans-serif;font-size:23px;color:#555}
.course-name{left:752px;top:2256px;width:215px;font-family:"Ubuntu",sans-serif;font-weight:700;color:var(--pink);font-size:19px;line-height:24px}
.course-name small{font-size:16px;color:#444;font-weight:500}
.course-copy{left:752px;top:2310px;width:210px;font-size:13px;line-height:17px;color:#555}
.course-cover{left:978px;top:2240px;width:142px;height:209px;background:linear-gradient(135deg,#f3dfe8,#e2a9c0 50%,#c25a86)}

/* footer */
.footer{left:0;top:2458px;width:1200px;height:58px;background:var(--pink);color:#fff;font-size:13px}
.footer .links{position:absolute;left:42px;top:20px}
.footer .links a{color:#fff}
.footer .connect{position:absolute;left:862px;top:20px}
.circle{position:absolute;top:14px;width:30px;height:30px;border-radius:50%;background:#f06aa3}
</style>
</head>
<body>

<header class="hero abs">
  <div class="hero-figure abs" role="img" aria-label="Photo of a runner in a sports top, city skyline behind"></div>
  <div class="brand abs"><span class="brand-dot"></span>Bright Fork Kitchen</div>
  <nav class="nav abs">ABOUT BEATRIX<span>|</span>THE MAGAZINE<span>|</span>BLOG &amp; VIDEOS<span>|</span>SHOP</nav>
  <h1 class="hero-title abs">You don’t need another diet<br>to get the body you want</h1>
</header>

<section class="optin abs">
  <h2>Get my FREE monthly E-Magazine</h2>
  <p>With delicious recipes, inspirational articles, workouts &amp; expert wellness tips that acually work! Yup FREE!</p>
  <div class="envelope"></div>
  <div class="field" style="left:606px;top:33px;width:188px">First Name</div>
  <div class="field" style="left:802px;top:33px;width:188px">Email</div>
  <div class="btn" style="left:999px;top:33px;width:150px;height:29px;line-height:29px;font-size:14px">Yes Please!</div>
</section>

<main class="main abs">
  <h1>Want a Body You’re Proud Of AND a Healthy Lifestyle You Love? Then You Don’t Need Another Diet!</h1>
  <p>Hey there I’m Beatrix. I help smart, savvy, driven women just like you to slim down so you can not only rock your outfit but you can enjoy a lifestyle to match. As hard as it might be for you to believe right now, I’ll teach you how to have this in a way that’s easier, and heaps more enjoyable than you’d ever thought possible – it’s time to kiss guilt and deprivation goodbye!</p>

  <div class="video">
    <div class="video-still" role="img" aria-label="Video still of Beatrix talking outdoors by a river with city towers"></div>
    <div class="play"></div>
    <div class="video-bar"></div>
  </div>

  <h3 style="margin-top:36px">Hmmm… do any of these sound familiar?</h3>
  <ul class="ticks" style="margin-top:8px">
    <li>Tried a bunch of diet plans but you’re still stuck in body that just feels yuk</li>
    <li>You “know what to do” but somehow you’re still not doing it (WTF!)</li>
    <li>Suffer from emotional eating, feelings of guilt or frustration around food &amp; exercise</li>
    <li>Feel bloated, guilty and maybe even a bit ashamed</li>
    <li>Overwhelmed and frustrated at yourself, feel that being slim and fit is a never ending chore</li>
  </ul>
  <p>You’re not the only one… heck that was me at one time. But if you’re exhausted at not liking your body, and sick of seeing other women make it all look so easy, don’t you think maybe it’s time to try something new? Perhaps it’s time you stopped following what everyone else is doing (girlfriends, the 19 year old receptionist at work, or that really buffed chick at the gym)… obviously it’s not working. So what’s the alternative?</p>

  <h3 style="margin-top:14px">What If I Told You There Was An Easier &amp; More Enjoyable Way?</h3>
  <ul class="ticks" style="margin-top:6px">
    <li>To Lose weight (most ladies I work with want to lose between 5kg-10kg… sometimes more)</li>
    <li>Have more energy</li>
    <li>Stop feeling bloated and exhausted</li>
    <li>Stop feeling frustrated for eating the “wrong” things and not exercising “enough”</li>
    <li>Feel hot in your clothes, at work and when you go out</li>
    <li>Feel proud of yourself</li>
    <li>Still have a social life… with you know, friends and stuff!</li>
  </ul>
  <p>Ok… sounds good so far right, but you’re probably wondering what is about my method that’s so different for all the others out there? Honestly, the problem with most other diet programs is that they:</p>
  <ul class="ticks" style="margin-top:8px">
    <li>Ignore the importance of pleasure in your life for weight loss. (I think it’s key)</li>
    <li>Aren’t sustainable– (try and stop me from never eating a French pastry again &amp; see what happens)</li>
    <li>Don’t teach you how to never need to be on another program, plan or diet again.</li>
    <li>Focus on what you need to cut out (I focus on what you need more of in your life to make it more pleasurable so you can stop feeding the voids in your life with toxic food, booze, etc)</li>
    <li>Assume you want the same things as everyone else. They assume your definition of healthy should be the same as everyone else’s. (I’ll teach you what works for you)</li>
    <li>Ignore the impact that stress has on your ability to shift weight (biochemistry can be cruel).</li>
  </ul>
  <p style="margin-top:18px">I get it. I know and understand first hand your frustrations (I used to be you). <b style="color:#333">I know you want it to be effortless. I know you want to not worry about putting on weight EVER, you want to just “Be”.</b> You may have some pieces of the puzzle already, but they just never seem to gel together for long enough to get the outcome you truly crave – A hot body you’re proud of with a healthy lifestyle you love. I get it. I understand. And I can help you get there.</p>
  <p style="margin-top:18px">As a qualified Food &amp; Wellness Coach (and Personal Trainer), I’ve helped thousands of women (starting with myself) just like you over the last 7+ years to not just lose weight (that’s nice) but take back control, regain self confidence and find peace with their bodies (that’s better – trust me). You can do it to.</p>
  <p style="margin-top:18px">So what now? First things first, sign up for my E-Magazine below (it’s FREE!) to receive some really fantastic recipes, inspirational articles, workouts &amp; expert wellness tips each month.</p>
</main>

<aside>
  <div class="side found abs">
    <h4>ALREADY DISCOVERED BY:</h4>
    <div class="badge" style="left:80px;top:36px;width:140px"></div>
    <div class="badge" style="left:14px;top:70px;width:90px;height:34px"></div>
    <div class="badge" style="left:80px;top:112px;width:140px"></div>
    <div class="badge" style="left:14px;top:146px;width:160px;height:28px"></div>
  </div>
  <div class="side kick abs" role="img" aria-label="Photo of Beatrix in a vest top">
    <div class="kick-band"><b>6 WEEK MOMENTUM + DETOX</b><span>A complete step by step program to get you on the path to a hotter, healthier &amp; happier you!</span></div>
  </div>
  <div class="side order abs">
    <div class="ribbon">ORDER TODAY</div>
    <div class="order-art" role="img" aria-label="Covers of the Bright Fork Kitchen Guide"></div>
    <p>Yours for the awesome price of just $9.95! (Valued $19.95) *Limited Time Only</p>
    <div class="buy"><span class="buy-bag"></span>BUY NOW<span class="buy-arrow"></span></div>
  </div>
  <div class="side emag abs">
    <div class="emag-art" role="img" aria-label="Stacked e-magazine issue covers"></div>
    <b>GLOW.FUEL.RENEW E-MAG</b>
    <span>Your’s FREE Every Month!</span>
    <div class="corner">FREE</div>
  </div>
  <div class="social-like abs"><i>Recommend</i><i>Share</i><span>You, Owen Pratley and 5,879 others recommend this.</span></div>
</aside>

<section class="lower-band abs">
</section>
<div class="portrait abs" role="img" aria-label="Photo of Beatrix in a purple top"></div>
<div class="mail-icon abs"></div>
<h2 class="lower-title abs">Get Slim, Boost Energy, And Create a Healthy Life You Love!</h2>
<p class="lower-copy abs">Subscribe to my FREE monthly e-magazine for heaps of awesome recipes, workouts &amp; advice!</p>
<div class="field" style="left:273px;top:2339px;width:188px;height:33px">First Name</div>
<div class="field" style="left:469px;top:2339px;width:188px;height:33px">Email</div>
<div class="btn" style="left:273px;top:2383px;width:384px;height:45px;line-height:45px;font-size:22px;background:var(--teal)">SIGN ME UP!</div>
<div class="cta-title abs">Need a hand getting started?</div>
<div class="course-name abs">6 WEEK TOTAL<br>MOMENTUM <small>Course</small></div>
<p class="course-copy abs">Finally an easy to follow program to help you get slim &amp; eat well, but also help you create a Healthy Life you love!</p>
<div class="btn" style="left:752px;top:2402px;width:148px;height:27px;line-height:27px;font-size:13px">GET IT NOW!</div>
<div class="course-cover abs" role="img" aria-label="Cover of the 6 Week Total Momentum Course"></div>

<footer class="footer abs">
  <div class="links"><a href="#">Privacy Policy</a> | <a href="#">Returns &amp; Refunds</a> | <a href="#">Contact</a></div>
  <div class="connect">Connect with Beatrix</div>
  <span class="circle" style="left:1008px"></span>
  <span class="circle" style="left:1044px"></span>
  <span class="circle" style="left:1080px"></span>
  <span class="circle" style="left:1116px"></span>
</footer>

</body>
</html>
```